Expense Tracker App for Young Adults

I need a mobile app designer to design an app UI for me. It is for an expense tracker app. I’ve attached a mind map of the various screens and features of the app.

I would like to see designs for this app which is targeted towards young adults (late teens & early 20s) just starting their career who want to plan their budgets and track their expenses.
Updates

Hello designers! I'm conscious that this is not a guaranteed project, so I can understand that some of you might be apprehensive. Just wanted to let you know that I'm willing to see your initial drafts that show your direction and theme for design. You don't have to design the whole app. In fact, it's better if you share your initial design ideas so that we can have a discussion and I can give my input. If I see some good initial designs, I will be happy to make this a guaranteed project. I'm simply being cautious since I'm bootstrapping this and funding out of my own pocket. Thank you for your understanding!

Target Market(s)

Young adults who are just starting their careers, late teens and early 20s.

Font styles to use
Sans Serif

Requirements
Must have
• Ease of use, smart and sleek, a guided setup wizard which will help users setup their account after signing up.
Should not have
• Clunky

```html
<!DOCTYPE html>
<html lang="en">
<head>
<meta charset="utf-8">
<title>Expense Tracker App – Screens</title>
<link rel="stylesheet" href="https://fonts.googleapis.com/css2?family=Ubuntu:wght@400;500;700&family=Mukta:wght@400;500;600&display=swap">
<style>
  :root{
    --stage:#303030;
    --white:#ffffff;
    --ink:#22252e;
    --ink-soft:#4a4d57;
    --muted:#8a8d97;
    --faint:#c4c7d0;
    --surface:#f8f9fd;
    --green:#2ec99a;
    --green-light:#86e98f;
    --blue:#4a63d8;
    --navy:#223a6b;
    --coral:#f37b8c;
    --peach:#fba58a;
    --bar:#d3d8e4;
    --bar-fill:#2f6fdb;
    --on-green-top:#93eba0; --on-green-bottom:#2cadb9;
    --on-peach-top:#fcab84; --on-peach-bottom:#ef7191;
    --on-violet-top:#a5a3fb; --on-violet-bottom:#7163e9;
  }
  *{box-sizing:border-box;margin:0;padding:0}
  html,body{width:960px;height:1200px;overflow:hidden;background:var(--stage)}
  body{position:relative;font-family:"Ubuntu",sans-serif}

  .screen{position:absolute;width:375px;height:812px;transform:scale(.6);transform-origin:0 0;overflow:hidden}
  .abs{position:absolute}

  /* status bar */
  .status{position:absolute;left:16px;right:20px;top:14px;height:12px;font:500 9px "Mukta",sans-serif;display:flex;justify-content:space-between;align-items:center}
  .status svg{height:9px}

  /* onboarding */
  .onboard{color:var(--white)}
  .onboard--green{background:linear-gradient(var(--on-green-top),var(--on-green-bottom))}
  .onboard--peach{background:linear-gradient(var(--on-peach-top),var(--on-peach-bottom))}
  .onboard--violet{background:linear-gradient(var(--on-violet-top),var(--on-violet-bottom))}
  .onboard .status{color:var(--white)}
  .onboard__title{top:48px;width:100%;text-align:center;font-size:19px;font-weight:500}
  .onboard__art{left:20px;top:160px;width:335px;height:244px;border-radius:14px;background:rgba(255,255,255,.14)}
  .onboard__ground{left:20px;top:404px;width:331px;height:2px;background:var(--navy)}
  .onboard__caption{top:507px;width:100%;text-align:center;font:400 14.5px/20px "Mukta",sans-serif}
  .dots{top:571px;width:100%;display:flex;justify-content:center;gap:14px}
  .dots i{width:7px;height:7px;transform:rotate(45deg);background:rgba(255,255,255,.4)}
  .dots i.on{background:var(--white)}
  .btn{position:absolute;display:flex;align-items:center;justify-content:center;border-radius:26px;font-size:17px;font-weight:500}
  .btn--signup{left:37px;top:639px;width:302px;height:50px;background:var(--white);color:var(--ink);box-shadow:0 6px 16px rgba(0,0,0,.1)}
  .btn--outline{left:35px;top:711px;width:305px;height:46px;border:1.5px solid var(--white);color:var(--white)}
  .home-bar{left:128px;top:798px;width:120px;height:3px;border-radius:2px;background:rgba(255,255,255,.5)}

  /* light screens */
  .light{background:var(--surface);color:var(--ink)}
  .light .status{color:var(--ink)}
  .topbar{position:absolute;left:0;top:0;width:100%;height:124px;background:var(--white)}
  .page-title{top:49px;width:100%;text-align:center;font-size:17px;font-weight:500}
  .green-btn{background:linear-gradient(90deg,var(--green-light),var(--green));color:var(--white);box-shadow:0 6px 16px rgba(46,201,154,.3)}
  .card{position:absolute;background:var(--white);border-radius:10px;box-shadow:0 4px 18px rgba(30,40,80,.04)}
  .field{position:absolute;left:17px;width:302px;height:52px;border-radius:26px;background:var(--white);box-shadow:0 4px 16px rgba(30,40,80,.07);padding-left:20px;display:flex;align-items:center;font:400 14px "Mukta",sans-serif;color:var(--muted)}
  .link{top:611px;font:500 13px "Mukta",sans-serif;color:var(--green)}

  .tabs{position:absolute;left:0;top:98px;width:100%;font:400 12px "Mukta",sans-serif;color:var(--ink-soft)}
  .tabs span{position:absolute}
  .tabs .active{color:var(--green);font-weight:600}
  .tabs .underline{top:22px;left:133px;width:107px;height:2px;background:var(--ink-soft)}

  .nav{position:absolute;left:0;top:730px;width:100%;height:82px;background:var(--white)}
  .nav__item{position:absolute;top:18px;width:60px;text-align:center;font:600 10px "Mukta",sans-serif;color:var(--faint)}
  .nav__item svg{display:block;margin:0 auto 4px;width:26px;height:24px}
  .nav__item.on{color:var(--green)}
  .fab{position:absolute;left:164px;top:705px;width:48px;height:48px;border-radius:50%;background:linear-gradient(var(--green-light),var(--green));box-shadow:0 6px 14px rgba(46,201,154,.35);display:flex;align-items:center;justify-content:center}

  .stat{position:absolute;top:146px;height:110px;border-radius:8px;color:var(--white);padding:20px 0 0 20px}
  .stat--spent{left:20px;width:159px;background:linear-gradient(135deg,var(--coral),var(--peach))}
  .stat--earned{left:192px;width:162px;background:linear-gradient(135deg,var(--green),var(--green-light))}
  .stat__label{font:500 13px "Mukta",sans-serif}
  .stat__amount{font-size:20px;font-weight:700;margin-top:4px}
  .stat__note{font:500 11px "Mukta",sans-serif;margin-top:6px}
  .row{position:absolute;left:15px;right:14px;display:flex;align-items:center;font-size:13px}
  .row__icon{width:44px;height:44px;border-radius:50%;display:flex;align-items:center;justify-content:center;margin-right:12px}
  .row__amt{margin-left:auto;font:400 13px "Mukta",sans-serif;color:var(--ink-soft)}
</style>
</head>
<body>

<!-- onboarding 1 -->
<section class="screen onboard onboard--green" style="left:80px;top:73px">
  <div class="status"><span>9:41 AM</span><svg viewBox="0 0 40 10"><rect x="0" y="6" width="2" height="4" fill="#fff"/><rect x="3" y="4" width="2" height="6" fill="#fff"/><rect x="6" y="2" width="2" height="8" fill="#fff"/><rect x="9" y="0" width="2" height="10" fill="#fff"/><path d="M15 4a6 6 0 0 1 8 0l-4 5z" fill="#fff"/><rect x="27" y="1" width="12" height="8" rx="2" fill="#fff"/></svg></div>
  <h1 class="abs onboard__title">Expense Tracker App</h1>
  <div class="abs onboard__art" role="img" aria-label="Illustration of people with a bank card, wallet, banknotes and gold coins"></div>
  <div class="abs onboard__ground"></div>
  <p class="abs onboard__caption">Take control of your money<br>by tracking your expenses, adding goals</p>
  <div class="abs dots"><i class="on"></i><i></i><i></i></div>
  <div class="btn btn--signup">Sign Up</div>
  <div class="btn btn--outline">Login</div>
  <div class="abs home-bar"></div>
</section>

<!-- onboarding 2 -->
<section class="screen onboard onboard--peach" style="left:368px;top:73px">
  <div class="status"><span>9:41 AM</span><svg viewBox="0 0 40 10"><rect x="0" y="6" width="2" height="4" fill="#fff"/><rect x="3" y="4" width="2" height="6" fill="#fff"/><rect x="6" y="2" width="2" height="8" fill="#fff"/><rect x="9" y="0" width="2" height="10" fill="#fff"/><path d="M15 4a6 6 0 0 1 8 0l-4 5z" fill="#fff"/><rect x="27" y="1" width="12" height="8" rx="2" fill="#fff"/></svg></div>
  <h1 class="abs onboard__title">Expense Tracker App</h1>
  <div class="abs onboard__art" role="img" aria-label="Illustration of a person sitting on a chair thinking about a wallet with money, next to a plant"></div>
  <div class="abs onboard__ground"></div>
  <p class="abs onboard__caption">Keep track of every penny and see where<br>your money is going</p>
  <div class="abs dots"><i></i><i class="on"></i><i></i></div>
  <div class="btn btn--signup">Sign Up</div>
  <div class="btn btn--outline">Login</div>
  <div class="abs home-bar"></div>
</section>

<!-- onboarding 3 -->
<section class="screen onboard onboard--violet" style="left:655px;top:73px">
  <div class="status"><span>9:41 AM</span><svg viewBox="0 0 40 10"><rect x="0" y="6" width="2" height="4" fill="#fff"/><rect x="3" y="4" width="2" height="6" fill="#fff"/><rect x="6" y="2" width="2" height="8" fill="#fff"/><rect x="9" y="0" width="2" height="10" fill="#fff"/><path d="M15 4a6 6 0 0 1 8 0l-4 5z" fill="#fff"/><rect x="27" y="1" width="12" height="8" rx="2" fill="#fff"/></svg></div>
  <h1 class="abs onboard__title">Expense Tracker App</h1>
  <div class="abs onboard__art" role="img" aria-label="Illustration of two people putting large gold coins into a savings jar"></div>
  <div class="abs onboard__ground"></div>
  <p class="abs onboard__caption">Plan wisely with budgets, cut back on extras<br>and start saving for your dreams</p>
  <div class="abs dots"><i></i><i></i><i class="on"></i></div>
  <div class="btn btn--signup">Sign Up</div>
  <div class="btn btn--outline">Login</div>
  <div class="abs home-bar"></div>
</section>

<!-- log in -->
<section class="screen light" style="left:80px;top:640px">
  <div class="status"><span>9:41</span><svg viewBox="0 0 40 10"><rect x="0" y="6" width="2" height="4" fill="#22252e"/><rect x="3" y="4" width="2" height="6" fill="#22252e"/><rect x="6" y="2" width="2" height="8" fill="#22252e"/><rect x="9" y="0" width="2" height="10" fill="#22252e"/><path d="M15 4a6 6 0 0 1 8 0l-4 5z" fill="#22252e"/><rect x="27" y="1" width="12" height="8" rx="2" fill="#22252e"/></svg></div>
  <svg class="abs" style="left:20px;top:54px" width="24" height="12" viewBox="0 0 24 12"><path d="M23 6H2M7 1 2 6l5 5" stroke="#22252e" stroke-width="1.6" fill="none"/></svg>
  <h1 class="abs page-title">Log In</h1>
  <div class="btn green-btn" style="left:33px;top:118px;width:312px;height:50px">Connect with Nimbus</div>
  <div class="btn" style="left:33px;top:190px;width:311px;height:50px;background:var(--blue);color:var(--white)">Connect with Circlo</div>
  <div class="abs" style="left:20px;top:296px;width:136px;height:2px;background:var(--navy)"></div>
  <div class="abs" style="left:0;top:286px;width:100%;text-align:center;font-size:17px">OR</div>
  <div class="abs" style="left:213px;top:296px;width:136px;height:2px;background:var(--navy)"></div>
  <div class="card" style="left:20px;top:350px;width:335px;height:400px">
    <div class="field" style="top:34px">Email Address</div>
    <div class="field" style="top:102px">Password</div>
    <div class="btn green-btn" style="left:17px;top:181px;width:302px;height:50px">Log In</div>
    <span class="abs link" style="left:33px;top:260px">Sign Up</span>
    <span class="abs link" style="left:190px;top:258px">Forgot Password?</span>
  </div>
</section>

<!-- activity empty -->
<section class="screen light" style="left:368px;top:640px">
  <div class="topbar"></div>
  <div class="status"><span>9:41</span><svg viewBox="0 0 40 10"><rect x="0" y="6" width="2" height="4" fill="#22252e"/><rect x="3" y="4" width="2" height="6" fill="#22252e"/><rect x="6" y="2" width="2" height="8" fill="#22252e"/><rect x="9" y="0" width="2" height="10" fill="#22252e"/><path d="M15 4a6 6 0 0 1 8 0l-4 5z" fill="#22252e"/><rect x="27" y="1" width="12" height="8" rx="2" fill="#22252e"/></svg></div>
  <div class="abs" style="left:20px;top:44px;width:32px;height:32px;border-radius:50%;background:linear-gradient(#8a6a62,#d8b4a6)" role="img" aria-label="Profile photo of the user"></div>
  <h1 class="abs page-title" style="font-size:15px;top:52px">Activity</h1>
  <svg class="abs" style="left:302px;top:52px" width="14" height="16" viewBox="0 0 14 16"><path d="M7 1a4.5 4.5 0 0 0-4.5 4.5V10L1 12h12l-1.5-2V5.5A4.5 4.5 0 0 0 7 1z" fill="#22252e"/><circle cx="7" cy="14" r="1.6" fill="#22252e"/></svg>
  <svg class="abs" style="left:350px;top:52px" width="4" height="16" viewBox="0 0 4 16"><circle cx="2" cy="2" r="1.8" fill="#22252e"/><circle cx="2" cy="8" r="1.8" fill="#22252e"/><circle cx="2" cy="14" r="1.8" fill="#22252e"/></svg>
  <div class="tabs"><span style="left:20px">August 2020</span><span class="active" style="left:140px">September 2020</span><span style="left:280px;top:2px">October 2020</span><span class="underline"></span></div>
  <div class="card" style="left:20px;top:174px;width:335px;height:330px;text-align:center;font:400 14.5px/20px 'Mukta',sans-serif">
    <p style="margin-top:24px">You don’t have any transaction.<br>at this moment, but you can</p>
    <div class="abs" style="left:107px;top:96px;width:120px;height:130px;border-radius:6px;background:linear-gradient(#eef0f7,#e3e6f2)" role="img" aria-label="Illustration of an empty transaction list with a pencil"></div>
    <p class="abs" style="left:0;top:256px;width:100%">Start adding one by pressing<br>the plus icon from the bottom menu</p>
  </div>
  <nav class="nav">
    <div class="nav__item on" style="left:19px"><svg viewBox="0 0 26 24"><rect x="2" y="3" width="22" height="6" fill="#2ec99a"/><rect x="2" y="12" width="22" height="9" fill="#2ec99a"/></svg>Activity</div>
    <div class="nav__item" style="left:92px"><svg viewBox="0 0 26 24"><rect x="6" y="1" width="14" height="22" rx="2" fill="#c4c7d0"/><rect x="8" y="3" width="10" height="5" fill="#fff"/></svg>Budget</div>
    <div class="nav__item" style="left:226px"><svg viewBox="0 0 26 24"><path d="M12 3a9 9 0 1 0 9 9h-9z" fill="#c4c7d0"/><path d="M14 1v9h9a9 9 0 0 0-9-9z" fill="#c4c7d0"/></svg>Reports</div>
    <div class="nav__item" style="left:298px"><svg viewBox="0 0 26 24"><rect x="2" y="5" width="22" height="16" rx="2" fill="#c4c7d0"/><rect x="15" y="11" width="9" height="5" fill="#fff"/></svg>Wallet</div>
  </nav>
  <div class="fab"><svg width="20" height="20" viewBox="0 0 20 20"><path d="M10 2v16M2 10h16" stroke="#fff" stroke-width="2.4"/></svg></div>
</section>

<!-- activity with data -->
<section class="screen light" style="left:655px;top:640px">
  <div class="topbar"></div>
  <div class="status"><span>9:41</span><svg viewBox="0 0 40 10"><rect x="0" y="6" width="2" height="4" fill="#22252e"/><rect x="3" y="4" width="2" height="6" fill="#22252e"/><rect x="6" y="2" width="2" height="8" fill="#22252e"/><rect x="9" y="0" width="2" height="10" fill="#22252e"/><path d="M15 4a6 6 0 0 1 8 0l-4 5z" fill="#22252e"/><rect x="27" y="1" width="12" height="8" rx="2" fill="#22252e"/></svg></div>
  <svg class="abs" style="left:20px;top:52px" width="14" height="16" viewBox="0 0 14 16"><path d="M7 1a4.5 4.5 0 0 0-4.5 4.5V10L1 12h12l-1.5-2V5.5A4.5 4.5 0 0 0 7 1z" fill="#22252e"/><circle cx="7" cy="14" r="1.6" fill="#22252e"/></svg>
  <h1 class="abs page-title" style="font-size:15px;top:52px">Activity</h1>
  <svg class="abs" style="left:350px;top:52px" width="4" height="16" viewBox="0 0 4 16"><circle cx="2" cy="2" r="1.8" fill="#22252e"/><circle cx="2" cy="8" r="1.8" fill="#22252e"/><circle cx="2" cy="14" r="1.8" fill="#22252e"/></svg>
  <div class="tabs"><span style="left:20px">August 2020</span><span class="active" style="left:140px">September 2020</span><span style="left:280px;top:2px">October 2020</span><span class="underline"></span></div>

  <div class="stat stat--spent"><div class="stat__label">Spent</div><div class="stat__amount">-$400.00</div><div class="stat__note">Expenses this month</div></div>
  <div class="stat stat--earned"><div class="stat__label">Earned</div><div class="stat__amount">+$680.00</div><div class="stat__note">Incomes this month</div></div>

  <div class="card" style="left:20px;top:278px;width:335px;height:102px">
    <div class="abs" style="left:15px;top:12px;font-size:15px;font-weight:500">Budget so far</div>
    <div class="abs" style="left:15px;top:48px;font:400 13px 'Mukta',sans-serif">$280.00</div>
    <div class="abs" style="right:14px;top:48px;font:400 13px 'Mukta',sans-serif">$1000.00</div>
    <div class="abs" style="left:15px;top:70px;width:304px;height:7px;border-radius:2px;background:var(--bar)"><div style="width:23%;height:100%;background:var(--bar-fill);border-radius:2px"></div></div>
  </div>

  <div class="card" style="left:20px;top:400px;width:335px;height:185px">
    <div class="abs" style="left:15px;top:12px;font-size:15px;font-weight:500">Today</div>
    <div class="abs" style="right:12px;top:14px;font:400 13px 'Mukta',sans-serif;color:var(--ink-soft)">-$1400.00</div>
    <div class="row" style="top:57px"><span class="row__icon" style="background:linear-gradient(135deg,var(--coral),var(--peach))"><svg width="16" height="14" viewBox="0 0 16 14"><path d="M8 1 1 7h2v6h4V9h2v4h4V7h2z" fill="#fff"/></svg></span>Rent<span class="row__amt">-$400.00</span></div>
    <div class="row" style="top:116px"><span class="row__icon" style="background:linear-gradient(135deg,var(--green),var(--green-light))"><svg width="16" height="16" viewBox="0 0 16 16" fill="none" stroke="#fff" stroke-width="1.2"><circle cx="8" cy="8" r="6.5"/><ellipse cx="8" cy="8" rx="3" ry="6.5"/><path d="M1.5 8h13M2.5 4.5h11M2.5 11.5h11"/></svg></span>Home Internet<span class="row__amt">-$150.00</span></div>
  </div>

  <nav class="nav">
    <div class="nav__item on" style="left:19px"><svg viewBox="0 0 26 24"><rect x="2" y="3" width="22" height="6" fill="#2ec99a"/><rect x="2" y="12" width="22" height="9" fill="#2ec99a"/></svg>Activity</div>
    <div class="nav__item" style="left:92px"><svg viewBox="0 0 26 24"><rect x="6" y="1" width="14" height="22" rx="2" fill="#c4c7d0"/><rect x="8" y="3" width="10" height="5" fill="#fff"/></svg>Budget</div>
    <div class="nav__item" style="left:226px"><svg viewBox="0 0 26 24"><path d="M12 3a9 9 0 1 0 9 9h-9z" fill="#c4c7d0"/><path d="M14 1v9h9a9 9 0 0 0-9-9z" fill="#c4c7d0"/></svg>Reports</div>
    <div class="nav__item" style="left:298px"><svg viewBox="0 0 26 24"><rect x="2" y="5" width="22" height="16" rx="2" fill="#c4c7d0"/><rect x="15" y="11" width="9" height="5" fill="#fff"/></svg>Wallet</div>
  </nav>
  <div class="fab"><svg width="20" height="20" viewBox="0 0 20 20"><path d="M10 2v16M2 10h16" stroke="#fff" stroke-width="2.4"/></svg></div>
</section>

</body>
</html>
```